Velmira - New coded website

Current website is around 5 years old and corrupted in some ways...
I would like to refresh the design and to create a new coded website based on the current content .
Please refer to :
www.velmira.com.au

Coding

Coded - Design and coding required

```html
<!DOCTYPE html>
<html lang="en">
<head>
<meta charset="utf-8">
<title>Velmira – Odours Controlled Naturally</title>
<link rel="stylesheet" href="https://fonts.googleapis.com/css2?family=Playfair+Display:wght@400;500&family=Plus+Jakarta+Sans:wght@400;500;600&display=swap">
<style>
:root{
  --green:#6ab43e;
  --green-dark:#4f9a2c;
  --navy:#0e2638;
  --blue:#1b4f7a;
  --ink:#1e2a33;
  --muted:#5b6670;
  --pale:#eef4f8;
  --white:#ffffff;
  --star:#f5a623;
}
*{box-sizing:border-box;margin:0;padding:0}
html,body{width:1200px;height:4707px;overflow:hidden}
body{position:relative;background:var(--white);font-family:"Plus Jakarta Sans",Arial,sans-serif;color:var(--ink)}
.abs{position:absolute}
.serif{font-family:"Playfair Display",Georgia,serif;font-weight:400}
.btn{position:absolute;display:flex;align-items:center;justify-content:center;gap:6px;background:var(--green);color:#fff;border-radius:20px;font-size:11px;font-weight:500}

/* header / hero */
.hero{left:0;top:0;width:1200px;height:563px;border-bottom-left-radius:120px;overflow:hidden;
  background:linear-gradient(180deg,#a9c3d6 0%,#7f9c8a 22%,#5f8a3a 45%,#4f7f2a 75%,#3b6a22 100%)}
.topbar{right:0;top:0;height:26px;display:flex;align-items:center}
.topbar .info{background:var(--green);height:26px;display:flex;align-items:center;gap:26px;padding:0 30px 0 40px;color:#fff;font-size:9px;clip-path:polygon(14px 0,100% 0,100% 100%,0 100%)}
.topbar .quote{background:var(--blue);color:#fff;height:26px;width:172px;display:flex;align-items:center;justify-content:center;font-size:10px;font-weight:500;margin-right:188px}
.brand{display:flex;align-items:center;gap:8px;color:#fff;font-size:24px;font-weight:500}
.brand .dot{width:34px;height:34px;border-radius:50%;background:var(--green)}
.nav{top:42px;left:386px;display:flex;gap:22px;color:#fff;font-size:10px}
.hero-eyebrow{left:188px;top:200px;color:#fff;font-size:15px;letter-spacing:2px}
.hero-title{left:188px;top:222px;color:#fff;font-size:48px;line-height:46px}
.hero-rule{left:384px;top:299px;width:170px;height:2px;background:var(--green)}

/* features */
.features{left:0;top:563px;width:1200px;height:369px;background:linear-gradient(120deg,#ffffff 0%,#e9f3fb 55%,#d6e9f7 100%)}
.feature{position:absolute;top:70px;width:190px;text-align:center}
.feature .ring{width:190px;height:190px;border-radius:50%;background:#fff;border:6px solid #d6e4ec;box-shadow:0 8px 20px rgba(0,40,70,.12);display:flex;align-items:center;justify-content:center}
.feature .label{margin-top:22px;font-size:27px}

.photo-band{left:0;top:932px;width:1200px;height:456px;background:linear-gradient(180deg,#8aa0a8 0%,#b99a5e 35%,#a5813f 70%,#7d6230 100%)}

/* video */
.video-band{left:0;top:1388px;width:1200px;height:375px;background:linear-gradient(180deg,#5fae3c 0%,#3d8a55 45%,#1e5c78 80%,#16496f 100%)}
.video-title{left:0;top:1470px;width:1200px;text-align:center;color:#fff;font-size:34px}
.video-card{left:188px;top:1551px;width:826px;height:381px;border-radius:30px;overflow:hidden;background:#fbfdf6;box-shadow:0 14px 30px rgba(0,0,0,.12)}
.video-art{position:absolute;inset:0;background:linear-gradient(180deg,#fbfdf6 0%,#fbfdf6 55%,#9fd36b 78%,#1f8a7a 100%)}
.play{left:554px;top:1696px;width:94px;height:94px;border-radius:50%;background:#14232e;display:flex;align-items:center;justify-content:center}

/* about */
.about-photo{left:188px;top:2002px;width:402px;height:402px;border-radius:50%;border:5px solid var(--green);padding:12px;background:#fff}
.about-photo .fill{width:100%;height:100%;border-radius:50%;background:radial-gradient(circle at 50% 40%,#c9a58a 0%,#8c6a58 45%,#3c3a3d 100%)}
.about-badge{left:470px;top:2262px;width:142px;height:142px;border-radius:50%;background:var(--green);border:8px solid #fff}
.about-text{left:663px;top:2068px;width:370px}
.about-text h2{font-size:36px;margin-bottom:12px}
.about-text p{font-size:11.5px;line-height:19px;color:var(--muted);margin-bottom:18px}

/* best */
.best-text{left:188px;top:2574px;width:380px}
.best-text h2{font-size:36px;line-height:38px;margin-bottom:20px}
.best-text p{font-size:11.5px;line-height:19px;color:var(--muted);margin-bottom:22px}
.ticks{list-style:none}
.ticks li{display:flex;align-items:center;gap:8px;font-size:12px;color:var(--muted);height:30px}
.best-green{left:645px;top:2520px;width:330px;height:415px;background:var(--green);transform:rotate(-15deg);transform-origin:center}
.best-photo{left:667px;top:2535px;width:307px;height:408px;background:linear-gradient(180deg,#d9e8f4 0%,#a9c9e2 28%,#3f7a2c 48%,#5f9e36 65%,#8cc64a 100%)}

/* testimonials */
.testi-band{left:0;top:2995px;width:1200px;height:667px;background:linear-gradient(180deg,#f4f8fb 0%,#e8f0f6 100%)}
.testi-title{left:0;top:3136px;width:1200px;text-align:center;font-size:36px}
.card{position:absolute;top:3224px;width:628px;height:334px;border-radius:10px;background:#fff;padding:34px 36px;box-shadow:0 8px 24px rgba(0,40,70,.08)}
.card p{font-size:12.5px;line-height:27.5px;color:var(--muted)}
.card.active{background:var(--green)}
.card.active p{color:#fff}
.card .foot{position:absolute;left:36px;right:36px;bottom:18px;display:flex;align-items:center;gap:12px;border-top:1px solid rgba(0,0,0,.08);padding-top:14px}
.card.active .foot{border-top-color:rgba(255,255,255,.3)}
.avatar{width:34px;height:34px;border-radius:50%;background:#c7b7cf}
.who b{display:block;font-family:"Playfair Display",Georgia,serif;font-size:14px;font-weight:500}
.who span{font-size:9px}
.card.active .who{color:#fff}
.stars{margin-left:auto;color:var(--star);font-size:16px;letter-spacing:8px}

/* contact */
.touch-title{left:0;top:3744px;width:1200px;text-align:center;font-size:34px}
.touch-item{position:absolute;top:3823px;display:flex;align-items:center;gap:16px}
.touch-item .ic{width:70px;height:70px;border-radius:50%;background:var(--green);display:flex;align-items:center;justify-content:center}
.touch-item b{display:block;font-family:"Playfair Display",Georgia,serif;font-weight:500;font-size:15px;margin-bottom:4px}
.touch-item span{font-size:10px;color:var(--muted);line-height:14px;display:block}
.navy{left:0;top:4069px;width:1200px;height:638px;background:var(--navy)}
.contact-card{left:188px;top:3927px;width:826px;height:305px;background:#fff;border-radius:8px;box-shadow:0 10px 30px rgba(0,0,0,.1)}
.contact-card h2{position:absolute;top:36px;width:100%;text-align:center;font-size:34px}
.field{position:absolute;background:#f0f2f4;border-radius:4px;font-size:10px;color:#7a848c;padding:14px 16px}

/* newsletter & footer */
.news-title{left:188px;top:4292px;color:#fff;font-size:30px;line-height:36px}
.news-form{left:608px;top:4305px;width:406px;height:40px;display:flex;border-radius:20px;overflow:hidden}
.news-form .input{flex:1;background:#1d3548;color:#9fb0bd;font-size:10px;display:flex;align-items:center;gap:8px;padding-left:22px}
.news-form .send{width:118px;background:var(--green);color:#fff;font-size:11px;display:flex;align-items:center;justify-content:center;gap:6px}
.foot-brand{left:188px;top:4436px}
.links{left:416px;top:4448px;color:#fff}
.links h4{font-family:"Playfair Display",Georgia,serif;font-weight:400;font-size:15px;margin-bottom:14px}
.links li{list-style:none;font-size:10px;color:#b7c4cd;line-height:23px}
.links li::before{content:"•";margin-right:6px;color:var(--green)}
.map{left:608px;top:4427px;width:406px;height:172px;border-radius:6px;background:linear-gradient(135deg,#eef1f3,#dfe6ea)}
.legal{left:188px;top:4674px;width:826px;display:flex;font-size:9.5px;color:#9fb0bd}
.legal .right{margin-left:auto;display:flex;gap:14px}
</style>
</head>
<body>

<!-- Hero -->
<header class="abs hero" role="img" aria-label="Photo of a woman resting in a green alpine meadow with hills behind">
</header>
<div class="abs topbar">
  <div class="info"><span>☎ +61 (08) 5550 2741</span><span>✉ info@velmira.com</span></div>
  <div class="quote">Request a Quote</div>
</div>
<div class="abs brand" style="left:188px;top:20px"><span class="dot"></span>Velmira</div>
<nav class="abs nav">
  <span>Odour Control Products</span><span>How Biofiltration Works</span><span>Odour Control by Industry</span><span>Past Projects</span><span>About Us</span><span>Contact</span>
</nav>
<div class="abs hero-eyebrow">Wellcome To Velmira</div>
<h1 class="abs hero-title serif">Odours Controlled<br>Naturally</h1>
<div class="abs hero-rule"></div>
<div class="btn" style="left:188px;top:342px;width:164px;height:36px">Request a Quote →</div>

<!-- Features -->
<section class="abs features">
  <div class="feature" style="left:232px">
    <div class="ring">
      <svg width="96" height="80" viewBox="0 0 96 80" fill="none" stroke="#6ab43e" stroke-width="3"><rect x="30" y="8" width="50" height="14"/><rect x="34" y="22" width="42" height="28"/><line x1="48" y1="30" x2="62" y2="30"/><path d="M6 46h10v26H6zM16 52h18l12 6h20l14-8"/><path d="M16 68h40l26-14"/></svg>
    </div><div class="label serif">Products</div>
  </div>
  <div class="feature" style="left:512px">
    <div class="ring">
      <svg width="86" height="80" viewBox="0 0 86 80" fill="none" stroke="#6ab43e" stroke-width="3"><circle cx="12" cy="14" r="7"/><circle cx="12" cy="40" r="7"/><circle cx="12" cy="66" r="7"/><path d="M28 10h50M28 18h42M28 36h50M28 44h42M28 62h50M28 70h42"/></svg>
    </div><div class="label serif">Features</div>
  </div>
  <div class="feature" style="left:791px">
    <div class="ring">
      <svg width="86" height="80" viewBox="0 0 86 80" fill="none" stroke="#6ab43e" stroke-width="3.5"><path d="M64 18A32 32 0 1 0 72 46"/><path d="M60 8l6 10-11 3"/><circle cx="40" cy="44" r="20"/><path d="M40 44V32M40 44l10 6"/></svg>
    </div><div class="label serif">Past Projects</div>
  </div>
</section>

<div class="abs photo-band" role="img" aria-label="Photo of a red-haired woman with arms outstretched in a golden grass field"></div>

<!-- Video -->
<section class="abs video-band"></section>
<h2 class="abs video-title serif">Watch Our Video</h2>
<div class="abs video-card">
  <div class="video-art" role="img" aria-label="Illustration of biofilter tanks among trees with icons for cost, savings, recycling and no odour"></div>
</div>
<div class="abs play"><svg width="24" height="24" viewBox="0 0 24 24"><path d="M8 5l12 7-12 7z" fill="#fff"/></svg></div>

<!-- About -->
<div class="abs about-photo"><div class="fill" role="img" aria-label="Portrait photo of a woman breathing fresh air with eyes closed"></div></div>
<div class="abs about-badge"></div>
<div class="abs about-text">
  <h2 class="serif">About Odours</h2>
  <p>Velmira uses sustainable biotechnology to resolve odour and corrosion problems in a highly efficient, environmentally friendly and cost-effective manner.</p>
  <p>Our products, the VelVent series of biofilters have been specifically engineered to overcome issues traditionally associated with biofiltration, such as bed compaction and uneven moisture levels, and our patented design achieves a removal rate of up to 99.9% per stage of treatment.</p>
</div>
<div class="btn" style="left:663px;top:2329px;width:164px;height:36px">Read More →</div>

<!-- Why us -->
<div class="abs best-text">
  <h2 class="serif">What makes us<br>the best?</h2>
  <p>It was popularised in the 1960s with the release of Presset sheets containing Lorem Ipsum passages, and more recently with desktop publishing software like Aldmark Layout.</p>
  <ul class="ticks">
    <li><svg width="16" height="16" viewBox="0 0 16 16" fill="none" stroke="#6ab43e" stroke-width="1.6"><circle cx="8" cy="8" r="7"/><path d="M4.5 8.2l2.3 2.3 4.7-4.8"/></svg>Biological &amp; Sustainable technology</li>
    <li><svg width="16" height="16" viewBox="0 0 16 16" fill="none" stroke="#6ab43e" stroke-width="1.6"><circle cx="8" cy="8" r="7"/><path d="M4.5 8.2l2.3 2.3 4.7-4.8"/></svg>Efficient maintenance cost</li>
    <li><svg width="16" height="16" viewBox="0 0 16 16" fill="none" stroke="#6ab43e" stroke-width="1.6"><circle cx="8" cy="8" r="7"/><path d="M4.5 8.2l2.3 2.3 4.7-4.8"/></svg>100% Australian Owned</li>
    <li><svg width="16" height="16" viewBox="0 0 16 16" fill="none" stroke="#6ab43e" stroke-width="1.6"><circle cx="8" cy="8" r="7"/><path d="M4.5 8.2l2.3 2.3 4.7-4.8"/></svg>Eco Friendly</li>
  </ul>
</div>
<div class="abs best-green"></div>
<div class="abs best-photo" role="img" aria-label="Photo of a green lawn with a row of leafy trees under a blue sky"></div>

<!-- Testimonials -->
<section class="abs testi-band"></section>
<svg class="abs" style="left:0;top:2960px" width="1200" height="140" viewBox="0 0 1200 140"><path d="M0 0H1200V60Q700 170 0 80Z" fill="#fff"/><path d="M0 80Q700 170 1200 60" fill="none" stroke="#6ab43e" stroke-width="6"/></svg>
<h2 class="abs testi-title serif">Our Testimonials</h2>
<div class="card" style="left:-373px">
  <p>"Ben and the Velmira team promised to stop the odour from our smelly neighbor and they delivered- in spades! As soon as the system was started, the smell disappeared. The system is well designed, very professionally installed and the beauty of it is, apart from a constantly running fan, it is bacteria doing the heavy lifting, so it is very environmentally friendly. We lived with the smell for 3 three years which could be extremely frustrating and unpleasant. Now, the problem is solved and we can have BBQs again. We are happy and our neighbours have</p>
  <div class="foot"><span class="stars">★★★★★</span></div>
</div>
<div class="card active" style="left:287px">
  <p>"Ben and the Velmira team promised to stop the odour from our smelly neighbor and they delivered- in spades! As soon as the system was started, the smell disappeared. The system is well designed, very professionally installed and the beauty of it is, apart from a constantly running fan, it is bacteria doing the heavy lifting, so it is very environmentally friendly. We lived with the smell for 3 three years which could be extremely frustrating and unpleasant. Now, the problem is solved and we can have BBQs again. We are happy and our neighbours have noticed the odour is gone. Thank you!"</p>
  <div class="foot"><span class="avatar"></span><div class="who"><b>Liam.</b><span>Designation Here</span></div><span class="stars">★★★★★</span></div>
</div>
<div class="card" style="left:939px">
  <p>"Ben and the Velmira team promised to stop the odour from our smelly neighbor and they delivered- in spades! As soon as the system was started, the smell disappeared. The system is well designed, very professionally installed and the beauty of it is, apart from a constantly running fan, it is bacteria doing the heavy lifting, so it is very environmentally friendly. We lived with the smell for 3 three years which could be extremely frustrating and unpleasant. Now, the problem is solved and we can have BBQs again. We are happy and our neighbours have noticed the odour is gone. Thank you!"</p>
  <div class="foot"><span class="avatar"></span><div class="who"><b>Grant</b><span>Designation Here</span></div></div>
</div>

<!-- Get in touch -->
<h2 class="abs touch-title serif">Get In Touch</h2>
<div class="touch-item" style="left:250px">
  <div class="ic"><svg width="26" height="26" viewBox="0 0 26 26" fill="none" stroke="#fff" stroke-width="2"><circle cx="13" cy="13" r="8"/><circle cx="13" cy="13" r="3" fill="#fff"/><path d="M13 1v4M13 21v4M1 13h4M21 13h4"/></svg></div>
  <div><b>Address</b><span>14 Harwick Lane, Kelmscott<br>WA 6111, Australia</span></div>
</div>
<div class="touch-item" style="left:518px">
  <div class="ic"><svg width="26" height="26" viewBox="0 0 24 24"><path d="M6.6 10.8a15 15 0 0 0 6.6 6.6l2.2-2.2a1 1 0 0 1 1-.25 11.4 11.4 0 0 0 3.6.57 1 1 0 0 1 1 1V20a1 1 0 0 1-1 1A17 17 0 0 1 3 4a1 1 0 0 1 1-1h3.5a1 1 0 0 1 1 1c0 1.25.2 2.45.57 3.57a1 1 0 0 1-.25 1z" fill="#fff"/></svg></div>
  <div><b>Phone</b><span>+61 (08) 5550 2741</span></div>
</div>
<div class="touch-item" style="left:760px">
  <div class="ic"><svg width="26" height="22" viewBox="0 0 26 22"><rect x="1" y="2" width="24" height="18" rx="2" fill="#fff"/><path d="M2 4l11 8 11-8" fill="none" stroke="#6ab43e" stroke-width="2"/></svg></div>
  <div><b>Email</b><span>info@velmira.com</span></div>
</div>

<div class="abs navy"></div>
<div class="abs contact-card">
  <h2 class="serif">Contact Us</h2>
  <div class="field" style="left:90px;top:86px;width:206px;height:42px">Name</div>
  <div class="field" style="left:310px;top:86px;width:206px;height:42px">Email</div>
  <div class="field" style="left:532px;top:86px;width:206px;height:42px">Phone</div>
  <div class="field" style="left:90px;top:142px;width:648px;height:74px">Message</div>
  <div class="btn" style="left:338px;top:238px;width:164px;height:36px">Submit Now →</div>
</div>

<!-- Newsletter -->
<h2 class="abs news-title serif">Sign Up For Our<br>Newsletter</h2>
<div class="abs news-form">
  <div class="input">✉ Enter Email Address</div>
  <div class="send">Submit Now →</div>
</div>

<!-- Footer -->
<div class="abs brand foot-brand"><span class="dot"></span>Velmira</div>
<div class="abs links">
  <h4>Quick Links</h4>
  <ul><li>Odour Control Products</li><li>How Biofiltration Works</li><li>Odour Control by Industry</li><li>Past Projects</li><li>About Us</li></ul>
</div>
<div class="abs map" role="img" aria-label="Street map showing the Kelmscott office location"></div>
<div class="abs legal">
  <span>© 2023 velmira.com All Rights Reserved</span>
  <span class="right"><span>Privacy Policy</span><span>|</span><span>Sitemap</span><span>|</span><span>ABN: 48 917 320 516</span></span>
</div>

</body>
</html>
```